Need Pexora Ads for Tyre Company

Need some pexora ads graphics for our tyre company Wheel Mates that only operates in the cayman islands.

Need Ratio Ads: 1000x1000, 1910x1000, 300x600

Important things to have the customer know:
-Email : info@wheelmates-demo.ky
-Phone: +1 345 555 0187
-Address: 41 Palmetto Lane, George Town, Cayman Islands
-Website: wheelmates-demo.ky (Please see our website for the tyres we offer)
- Common Car brands that our Tyres are compatible with: Ravello, Korvexa, Pip Talvo, Bexiline, Vardo, Pelmoro, Quendra, Strandmobil
- Our tyres are priced from KYD$55-$60
-We offer free installation on tyres when customers come to our facility to get them changed.
-We sell tyres in bulk and individually.

*You can choose which things to add or omit for the best look, feel free to reword any of the above also to better fit in.
*Please keep in mind that these will have to be viewed in small formats aswell since they are for pexora ads. Please ensure everything is readable when zoomed out.

Target Market(s)

car rental companies & individuals who need to get their tyres replace

Industry/Entity Type

Automotive, Tyre replacement, Car Parts

Colors
EB3D1F
EC4F4E
F09395
F8D3D4
FCEDEE

Requirements
Must have
• Phone, Location, Brands that our tyres are compatible with, Same theme as our logo(Red & Black, White), design adapted to the 3 ratios listed above
Nice to have
• Creative advertising

```html
<!DOCTYPE html>
<html lang="en">
<head>
<meta charset="utf-8">
<title>Wheel Mates – Tyre Ad 1200x2400</title>
<link rel="stylesheet" href="https://fonts.googleapis.com/css2?family=Roboto+Condensed:ital,wght@0,700;0,800;1,800;1,900&display=swap">
<style>
  :root {
    --red: #EB3D1F;
    --red-soft: #EC4F4E;
    --pink-mid: #F09395;
    --pink-light: #F8D3D4;
    --pink-bg: #FCEDEE;
    --ink: #1d1d1d;
    --slate: #3a3a3a;
    --blue: #2f5ea8;
    --grey-brand: #8a8a8a;
    --white: #ffffff;
  }
  * { box-sizing: border-box; margin: 0; padding: 0; }
  html, body { width: 1200px; height: 2400px; overflow: hidden; }
  body { font-family: "Roboto Condensed", "Arial Narrow", sans-serif; background: var(--pink-bg); }
  .ad {
    position: relative; width: 1200px; height: 2400px; overflow: hidden;
    background: linear-gradient(180deg, var(--pink-bg) 0%, #fbe4e5 100%);
  }
  .brand-name {
    position: absolute; top: 90px; left: 0; width: 1200px;
    display: flex; justify-content: center; align-items: center; gap: 30px;
  }
  .brand-name .dot { width: 70px; height: 70px; border-radius: 50%; background: var(--red); }
  .brand-name span {
    font-weight: 800; font-size: 184px; line-height: 1; color: var(--ink); letter-spacing: -2px;
  }
  .location {
    position: absolute; top: 330px; left: 0; width: 1200px;
    display: flex; justify-content: center; align-items: center; gap: 14px;
    font-weight: 700; font-size: 46px; color: var(--slate); white-space: nowrap;
  }
  .location svg { width: 40px; height: 52px; }
  .pill {
    position: absolute; left: 50%; transform: translateX(-50%);
    display: flex; align-items: center; justify-content: center; gap: 30px;
    border-radius: 70px; color: var(--white);
    font-weight: 900; font-style: italic; text-transform: uppercase; white-space: nowrap;
  }
  .pill--install { top: 464px; width: 672px; height: 120px; background: var(--red); font-size: 68px; }
  .pill--price { top: 632px; width: 760px; height: 136px; background: var(--red-soft); font-size: 72px; }
  .pill--range { top: 784px; width: 496px; height: 120px; background: var(--slate); font-size: 66px; font-weight: 800; }
  .pill--shop { top: 928px; width: 848px; height: 176px; background: var(--blue); font-size: 104px; }
  .pill--shop svg { width: 120px; height: 110px; }
  .makes {
    position: absolute; top: 1170px; left: 90px; width: 1020px;
    display: grid; grid-template-columns: repeat(4, 1fr); row-gap: 44px;
  }
  .make { display: flex; flex-direction: column; align-items: center; gap: 14px; }
  .make .mark { width: 116px; height: 116px; border-radius: 50%; background: var(--pink-light); border: 6px solid #c9c9c9; }
  .make span { font-weight: 700; font-size: 38px; color: var(--grey-brand); text-transform: uppercase; letter-spacing: 1px; }
  .swoosh { position: absolute; left: 0; top: 1680px; width: 1200px; height: 620px; }
  .tyre-photo {
    position: absolute; left: 170px; top: 1570px; width: 1400px; height: 1150px;
    border-radius: 50%; transform: rotate(-14deg);
    background: radial-gradient(ellipse at 62% 62%, #f0f0f0 0%, #c8c8c8 18%, #6a6a6a 30%, #2c2c2c 42%, #1a1a1a 62%, #111 100%);
  }
  .footer-bar {
    position: absolute; left: 0; bottom: 0; width: 1200px; height: 112px; z-index: 2;
    background: var(--red); display: flex; justify-content: space-between; align-items: center;
    padding: 0 36px; color: var(--white); font-weight: 800; font-style: italic; font-size: 52px;
  }
</style>
</head>
<body>
<main class="ad">
  <header class="brand-name">
    <div class="dot"></div>
    <span>Wheel Mates</span>
  </header>
  <p class="location">
    <svg viewBox="0 0 24 32" aria-hidden="true">
      <path d="M12 1C6 1 1.5 5.5 1.5 11.5 1.5 19 12 31 12 31s10.5-12 10.5-19.5C22.5 5.5 18 1 12 1z" fill="#EB3D1F"/>
      <circle cx="12" cy="11.5" r="4" fill="#fff"/>
    </svg>
    41 Palmetto Lane, George Town
  </p>

  <div class="pill pill--install">Free Installation</div>
  <div class="pill pill--price">Unbelievable Price</div>
  <div class="pill pill--range">KYD$55-$60</div>
  <div class="pill pill--shop">
    <svg viewBox="0 0 60 55" aria-hidden="true">
      <path d="M2 6h10l8 30h30l6-22H16" fill="none" stroke="#fff" stroke-width="5" stroke-linejoin="round" stroke-linecap="round"/>
      <path d="M22 20h28M24 28h24" stroke="#fff" stroke-width="4"/>
      <circle cx="24" cy="46" r="5" fill="#fff"/>
      <circle cx="46" cy="46" r="5" fill="#fff"/>
    </svg>
    Shop Now
  </div>

  <section class="makes" aria-label="Compatible car brands">
    <div class="make"><div class="mark"></div><span>Ravello</span></div>
    <div class="make"><div class="mark"></div><span>Korvexa</span></div>
    <div class="make"><div class="mark"></div><span>Talvo</span></div>
    <div class="make"><div class="mark"></div><span>Bexiline</span></div>
    <div class="make"><div class="mark"></div><span>Vardo</span></div>
    <div class="make"><div class="mark"></div><span>Quendra</span></div>
    <div class="make"><div class="mark"></div><span>Pelmoro</span></div>
    <div class="make"><div class="mark"></div><span>Strandmobil</span></div>
  </section>

  <svg class="swoosh" viewBox="0 0 1200 620" aria-hidden="true">
    <path d="M0 60 C 220 150, 340 380, 440 620 L0 620 Z" fill="var(--red)"/>
  </svg>
  <div class="tyre-photo" role="img" aria-label="Close-up of a car tyre with deep tread on a silver alloy wheel"></div>

  <footer class="footer-bar">
    <span>+1 345 555 0187</span>
    <span>www.wheelmates-demo.ky</span>
  </footer>
</main>
</body>
</html>
```